Anatomic 3D models + Urological Robotic surgery site

I want a website to represent my business as a developer of 3D models (reconstructions based on CT and MRI scans) and urological robotic surgery. The main point I need on my website is that it is modern, very attractive, clean, responsive and an interaction that differentiate me from the usual websites they have in my market. The site will be in portuguese and I'll provide the content to be used. The company name would be my name: Dr Renato Vilhena. The colors and other choices I made here are not final decisions. If you have a suggestion you, they are welcome.

Target Market(s)

My patients

Industry/Entity Type

Medical

Coding

Number of Pages Required

1 page

Font styles to use
Sans Serif

Colors
0054AA
0677BA
7BADD7
CADEEF
E8F1F8
0094D4
00A9DD
6FCCEA
C7EBF8
E9F6FB
00AB8E
00BBA5
67D7C9
C6EFE9
E9F9F6
59FF00
82FF00
B8FF75
E3FFCB
F4FFEA
FFC000
F8CF3A
FAE287
FDF2CF
FEFAEE
F0912C
F2A743
F7CA91
FBE8D2
FDF5EE
A7469A
B969AE
D3A5CF
EDDBEB
F8F0F9
6B429C
8869AF
B7A5CE
E3DAEB
F3F0F8

Requirements
Must have
• Responsive, clean, modern, attractive, stand out from usual sites.
Should not have
• Antiquate boring designs.

```html
<!DOCTYPE html>
<html lang="pt">
<head>
<meta charset="utf-8">
<title>Dr. Renato Vilhena — Urologia Robótica e Modelos 3D</title>
<link href="https://fonts.googleapis.com/css2?family=Poppins:wght@400;500;600;700&family=Inter:wght@400;500;600&display=swap" rel="stylesheet">
<style>
:root{
  --navy:#0a2f74;
  --blue:#0d4aa6;
  --primary:#0054AA;
  --accent:#0677BA;
  --sky:#7BADD7;
  --pale:#E8F1F8;
  --ink:#1c1f26;
  --muted:#6b7180;
  --white:#ffffff;
  --line:#cfd6e2;
}
*{box-sizing:border-box;margin:0;padding:0}
html,body{width:1200px;height:5286px;overflow:hidden}
body{font-family:"Poppins",sans-serif;color:var(--ink);background:var(--white);position:relative}
section,header,footer{position:absolute;left:0;width:1200px;overflow:hidden}
.abs{position:absolute}
.ph{position:absolute;border-radius:14px}
h2.section-title{font-family:"Inter",sans-serif;font-weight:400;font-size:38px;line-height:1.22;position:absolute}
.eyebrow{font-family:"Inter",sans-serif;font-weight:500;font-size:22px;position:absolute}
.btn{position:absolute;display:flex;align-items:center;justify-content:center;border-radius:30px;font-weight:600;font-size:14px}
.btn-blue{background:var(--primary);color:var(--white)}
.btn-white{background:var(--white);color:var(--navy)}

/* HERO */
.hero{top:0;height:728px;background:linear-gradient(120deg,#0b3a8c 0%,#0d4fb0 55%,#0a3b8e 100%);color:var(--white)}
.logo{font-weight:700;font-size:34px;letter-spacing:1px}
.nav a{position:absolute;top:38px;font-size:15px;color:var(--white);text-decoration:none}
.hero-title{left:60px;top:128px;font-size:96px;font-weight:700;line-height:1;letter-spacing:-1px}
.hero-sub{left:60px;top:248px;font-size:40px;font-weight:600}
.glass{position:absolute;border:1.5px solid rgba(255,255,255,.45);border-radius:26px;background:rgba(255,255,255,.08)}
.chip{position:absolute;border:1px solid rgba(255,255,255,.7);border-radius:20px;font-size:10px;padding:3px 12px;color:var(--white)}
.avatar{position:absolute;width:50px;height:50px;border-radius:50%;border:2px solid var(--white);background:linear-gradient(160deg,#c9a38a,#5a6b82)}

/* ABOUT */
.about{top:728px;height:677px}
.stat{position:absolute;top:1150px;width:180px;text-align:center}
.stat b{display:block;color:var(--primary);font-size:28px;font-weight:600}
.stat span{font-size:13px}

/* SERVICES */
.services{top:1405px;height:735px;background:linear-gradient(120deg,#0b3d92,#0a4aa8 60%,#0b3a88);color:var(--white)}
.service{position:absolute;left:60px;width:530px;height:70px}
.service .label{position:absolute;left:92px;top:16px;font-size:18px}
.service .rule{position:absolute;left:92px;right:0;top:58px;height:1px;background:rgba(255,255,255,.45)}

/* APPROACH */
.approach{top:2140px;height:985px}
.case{position:absolute;border-radius:16px;box-shadow:0 10px 30px rgba(0,0,0,.25);color:var(--white);font-weight:500}
.case span{position:absolute;left:0;right:0;text-align:center}

/* WHY */
.why{top:3125px;height:528px;background:linear-gradient(120deg,#0a3b8e,#0d4fb0 60%,#0b3d92);color:var(--white)}
.feature{position:absolute;background:var(--white);color:var(--ink);border-radius:8px;padding:18px 14px}
.feature h3{font-size:18px;font-weight:500;line-height:1.15;margin-left:58px;margin-bottom:16px;min-height:42px}
.feature p{font-size:14px;line-height:1.7;color:#333}
.feature svg{position:absolute;left:14px;top:18px}

/* FAQ */
.faq{top:3653px;height:554px}
.q{position:absolute;width:350px;height:118px;border-radius:12px;background:var(--white);box-shadow:0 4px 18px rgba(0,0,0,.12);padding:0 60px 0 18px;display:flex;align-items:center;font-family:"Inter",sans-serif;font-size:18px;line-height:1.45}
.q::after{content:"";position:absolute;right:18px;top:58px;width:12px;height:2px;background:var(--ink)}
.q-open{background:var(--navy);color:var(--white);padding:14px 16px;display:block;height:250px}
.q-open h4{font-family:"Inter",sans-serif;font-size:17px;font-weight:600;line-height:1.45;margin-bottom:14px;padding-right:24px}
.q-open p{font-size:13px;line-height:1.6;color:#b9c7e3}

/* CONTACT */
.contact{top:4207px;height:728px}
.field-label{position:absolute;font-size:14px}
.field-line{position:absolute;height:1px;background:#6d7480}

/* FOOTER */
.footer{top:4935px;height:351px;background:linear-gradient(120deg,#0a3b8e,#0d4fb0 60%,#0a3b8e);color:var(--white)}
.footer-nav a{position:absolute;top:5175px;font-size:15px;color:var(--white);text-decoration:none}
</style>
</head>
<body>

<header class="hero">
  <div class="abs logo" style="left:60px;top:26px">LOGO</div>
  <nav class="nav">
    <a style="left:250px">Home</a>
    <a style="left:340px">Dr. Renato Vilhena</a>
    <a style="left:514px">Serviços</a>
    <a style="left:622px">Nossa Abordagem</a>
    <a style="left:810px">Why Choose Me</a>
  </nav>
  <div class="btn btn-white" style="left:1010px;top:28px;width:132px;height:44px;font-size:15px;font-weight:500;color:var(--primary)">Contact Us</div>

  <h1 class="abs hero-title">Tecnologia de</h1>
  <p class="abs hero-sub">Precisão em Urologia Avançada</p>

  <div class="glass" style="left:60px;top:336px;width:258px;height:234px">
    <div class="abs" style="left:22px;top:24px;font-size:17px;line-height:1.4">Virtual<br>Consultation</div>
    <div class="abs" style="right:20px;top:22px;font-size:12px">24/7</div>
    <div class="chip" style="left:22px;top:100px">Consultation ↗</div>
    <div class="avatar" style="left:20px;top:162px" role="img" aria-label="Foto de paciente"></div>
    <div class="avatar" style="left:74px;top:162px" role="img" aria-label="Foto de paciente"></div>
    <div class="avatar" style="left:128px;top:162px" role="img" aria-label="Foto de paciente"></div>
    <div class="avatar" style="left:182px;top:162px" role="img" aria-label="Foto de paciente"></div>
  </div>
  <div class="abs" style="left:64px;top:585px;width:116px;height:34px;border:1.5px solid rgba(255,255,255,.7);border-radius:20px;font-size:16px;text-align:center;line-height:31px">Medication</div>
  <div class="abs" style="left:252px;top:590px;width:24px;height:24px;border-radius:50%;background:var(--white)"></div>
  <div class="abs" style="left:274px;top:590px;width:24px;height:24px;border-radius:50%;background:var(--pale)"></div>
  <div class="abs" style="left:296px;top:590px;width:24px;height:24px;border-radius:50%;background:var(--white)"></div>
  <div class="abs" style="left:60px;top:636px;width:258px;height:52px;border-radius:26px;background:var(--white)">
    <svg class="abs" style="left:18px;top:18px" width="16" height="16" viewBox="0 0 16 16"><circle cx="7" cy="7" r="5" fill="none" stroke="#8a94a6" stroke-width="1.6"/><line x1="11" y1="11" x2="15" y2="15" stroke="#8a94a6" stroke-width="1.6"/></svg>
    <span class="abs" style="left:48px;top:16px;font-size:12px;color:#9aa3b2">Search...</span>
    <div class="abs" style="right:8px;top:7px;width:38px;height:38px;border-radius:50%;background:var(--navy);color:var(--white);text-align:center;line-height:38px;font-size:14px">↗</div>
  </div>

  <div class="glass" style="left:396px;top:336px;width:168px;height:188px">
    <div class="chip" style="left:48px;top:14px">Statistics</div>
    <svg class="abs" style="left:30px;top:46px" width="108" height="108" viewBox="0 0 108 108">
      <circle cx="54" cy="54" r="44" fill="none" stroke="rgba(255,255,255,.25)" stroke-width="4"/>
      <circle cx="54" cy="54" r="44" fill="none" stroke="#fff" stroke-width="4" stroke-dasharray="235 276" transform="rotate(-90 54 54)"/>
      <text x="54" y="62" text-anchor="middle" font-family="Poppins,sans-serif" font-size="26" fill="#fff">85%</text>
    </svg>
    <div class="abs" style="left:0;right:0;top:158px;text-align:center;font-size:10px">Succesful diagnosis ↗</div>
  </div>
  <div class="ph" style="left:396px;top:540px;width:166px;height:150px;border-radius:22px;background:linear-gradient(135deg,#1b2a44,#3d5c8a 60%,#0e1b30)" role="img" aria-label="Médico analisando exames em monitores"></div>

  <div class="glass" style="left:578px;top:336px;width:166px;height:354px">
    <div class="abs" style="left:16px;top:22px;font-size:17px;line-height:1.4">Caring<br>Innovation</div>
    <div class="abs" style="left:16px;top:86px;background:var(--white);color:var(--primary);border-radius:14px;font-size:10px;padding:3px 12px">Explore ◎</div>
    <div class="chip" style="left:16px;top:212px">About</div>
    <div class="abs" style="left:16px;top:244px;width:140px;font-size:12px;line-height:1.6">AI enhances healthcare through personalized.....</div>
    <div class="abs" style="left:16px;top:316px;font-size:10px;font-style:italic">Read More</div>
  </div>

  <div class="ph" style="left:790px;top:160px;width:410px;height:560px;border-radius:50%;background:radial-gradient(ellipse at 50% 45%,rgba(200,60,50,.85) 0%,rgba(170,60,90,.5) 40%,rgba(13,79,176,0) 70%)" role="img" aria-label="Ilustração anatômica dos rins, ureteres e bexiga"></div>
</header>

<section class="about">
  <div class="eyebrow" style="left:60px;top:117px">Dr. Renato Vilhena</div>
  <h2 class="section-title" style="left:60px;top:160px">Avançando A Medicina Com<br>Tecnologia E Precisão</h2>
  <div class="ph" style="left:60px;top:300px;width:532px;height:262px;background:linear-gradient(135deg,#0d2b5c,#2f5f9e 55%,#0b2250)" role="img" aria-label="Equipe em sala de cirurgia robótica"></div>
  <div class="ph" style="left:610px;top:127px;width:256px;height:163px;background:linear-gradient(135deg,#1c3560,#4f73a6)" role="img" aria-label="Cirurgia robótica em andamento"></div>
  <div class="ph" style="left:884px;top:127px;width:256px;height:163px;background:linear-gradient(135deg,#152a4c,#56709a)" role="img" aria-label="Braços do robô cirúrgico"></div>
  <p class="abs" style="left:610px;top:324px;width:530px;font-size:14px;line-height:1.6;color:var(--muted)">Weve Been On Both Sides:Leading HOA Management Firms, Serving On Association Boards, And Training Professionals Across The Country. We Saw The Recurring Challenges:</p>
</section>
<div class="stat" style="left:592px"><b>15+</b><span>Years Of Experience</span></div>
<div class="stat" style="left:782px"><b>150+</b><span>Professional Values</span></div>
<div class="stat" style="left:976px"><b>1500+</b><span>Patient-Centered Care</span></div>
<div class="avatar" style="left:612px;top:1238px;border-color:#fff" role="img" aria-label="Foto de paciente"></div>
<div class="avatar" style="left:642px;top:1238px" role="img" aria-label="Foto de paciente"></div>
<div class="avatar" style="left:672px;top:1238px" role="img" aria-label="Foto de paciente"></div>
<div class="avatar" style="left:702px;top:1238px" role="img" aria-label="Foto de paciente"></div>
<div class="btn btn-blue" style="left:776px;top:1246px;width:136px;height:42px">Learn More</div>

<section class="services">
  <div class="eyebrow" style="left:60px;top:66px">Services</div>
  <h2 class="section-title" style="left:60px;top:98px">Precisão E Inovação Em Cada Passo<br>Do Tratamento</h2>
  <p class="abs" style="left:828px;top:88px;width:320px;font-size:14px;line-height:1.55">We provide a wide range of legal services tailored to meet the diverse needs of our clients.</p>

  <div class="service" style="top:230px">
    <svg width="58" height="58" viewBox="0 0 58 58" fill="none" stroke="#fff" stroke-width="2"><circle cx="29" cy="27" r="22"/><path d="M15 50h28M20 35h18M24 27a5 5 0 1 0 10 0a5 5 0 1 0-10 0"/></svg>
    <span class="label">3D Model Reconstruction from CT/MRI Scans</span><span class="rule"></span>
  </div>
  <div class="service" style="top:355px">
    <svg width="58" height="58" viewBox="0 0 58 58" fill="none" stroke="#fff" stroke-width="2"><rect x="20" y="6" width="18" height="12" rx="3"/><path d="M29 18v10M12 28h34M12 28l-4 18M46 28l4 18M20 28v14M38 28v14M6 50h46"/></svg>
    <span class="label">Robotic Urological Surgery</span><span class="rule"></span>
  </div>
  <div class="service" style="top:480px">
    <svg width="58" height="58" viewBox="0 0 58 58" fill="none" stroke="#fff" stroke-width="2"><rect x="6" y="30" width="46" height="14" rx="2"/><circle cx="20" cy="14" r="6"/><path d="M30 12h18M34 20h14M10 50h38"/></svg>
    <span class="label">Pre-Procedure Support</span><span class="rule"></span>
  </div>
  <div class="service" style="top:605px">
    <svg width="58" height="58" viewBox="0 0 58 58" fill="none" stroke="#fff" stroke-width="2"><path d="M29 48C14 38 8 30 8 22a10 10 0 0 1 21-5a10 10 0 0 1 21 5c0 8-6 16-21 26z"/><path d="M16 26h8l3-6 4 12 3-6h8"/></svg>
    <span class="label">Postoperative Care</span><span class="rule"></span>
  </div>

  <div class="ph" style="left:644px;top:235px;width:492px;height:430px;border-radius:20px;background:linear-gradient(135deg,#8fb4d8,#4d84c0 50%,#1c4f8f)" role="img" aria-label="Cirurgiã preparando instrumento em sala cirúrgica"></div>
</section>

<section class="approach">
  <div class="eyebrow" style="left:0;right:0;top:116px;text-align:center">Nossa Abordagem</div>
  <h2 class="section-title" style="left:0;right:0;top:144px;text-align:center">Precisão, Inovação E Cuidado</h2>

  <div class="case" style="left:150px;top:308px;width:250px;height:327px;background:linear-gradient(160deg,#5a6e8a,#2a3c58)" role="img" aria-label="Cirurgião em procedimento de câncer de bexiga"><span style="bottom:20px;font-size:14px;left:-30px">Surgery Bladder Cancer</span></div>
  <div class="case" style="left:800px;top:308px;width:250px;height:327px;background:linear-gradient(160deg,#2c5ea3,#0f2c5a)" role="img" aria-label="Equipamento cirúrgico com luzes azuis"><span style="bottom:20px;font-size:14px;left:30px">Male Reproductive Organs</span></div>
  <div class="case" style="left:378px;top:238px;width:444px;height:467px;background:linear-gradient(160deg,#3b4c66,#1a2538 70%)" role="img" aria-label="Cirurgia robótica de rim"><span style="bottom:24px;font-size:18px">Kidneys Robotic Surgery</span></div>

  <svg class="abs" style="left:0;top:660px" width="1200" height="120" viewBox="0 0 1200 120">
    <defs><linearGradient id="arc" x1="0" x2="1"><stop offset="0" stop-color="#0a2f74" stop-opacity="0"/><stop offset=".5" stop-color="#0a2f74"/><stop offset="1" stop-color="#0a2f74" stop-opacity="0"/></linearGradient></defs>
    <path d="M60 15 Q600 200 1140 15" fill="none" stroke="url(#arc)" stroke-width="3"/>
    <circle cx="268" cy="75" r="6" fill="#fff" stroke="#0054AA" stroke-width="3"/>
    <circle cx="932" cy="75" r="6" fill="#fff" stroke="#0054AA" stroke-width="3"/>
    <circle cx="600" cy="108" r="18" fill="#fff" stroke="#0054AA" stroke-width="4"/>
    <circle cx="600" cy="108" r="10" fill="#fff" stroke="#0054AA" stroke-width="3"/>
  </svg>
  <div class="btn btn-blue" style="left:520px;top:828px;width:160px;height:42px">Discover More</div>
</section>

<section class="why">
  <div class="eyebrow" style="left:58px;top:120px">Why Choose Me</div>
  <h2 class="section-title" style="left:58px;top:156px;font-size:40px">Precisão, Tecnologia E<br>Cuidado Real</h2>
  <p class="abs" style="left:58px;top:270px;width:470px;font-size:13px;line-height:1.65">Lorem Ipsum Dolor Sit Amet Consectetur. Velit Tortor Molestie Praesent Est Eget Etiam Consequat. Nibh Tristique Vel Ut Hac Odio Ut Tempor Turpis. Et Penatibus Ornare</p>
  <div class="btn btn-white" style="left:58px;top:375px;width:162px;height:42px">Discover More</div>

  <div class="feature" style="left:610px;top:65px;width:258px;height:155px">
    <svg width="44" height="44" viewBox="0 0 44 44" fill="none" stroke="#0054AA" stroke-width="2"><rect x="6" y="4" width="32" height="14" rx="3"/><path d="M22 18v8M8 26h28M10 26l-4 14M34 26l4 14"/></svg>
    <h3>High-Precision Robotic Surgery</h3><p>Identify And Mitigate Risks With Thorough Financial Analysis. We Help</p>
  </div>
  <div class="feature" style="left:610px;top:243px;width:258px;height:162px">
    <svg width="44" height="44" viewBox="0 0 44 44" fill="none" stroke="#0054AA" stroke-width="2"><circle cx="22" cy="14" r="8"/><path d="M6 40c2-9 9-14 16-14s14 5 16 14"/></svg>
    <h3>3D Planning for Every Patient</h3><p>Identify And Mitigate Risks With Thorough Financial Analysis. We Help</p>
  </div>
  <div class="feature" style="left:884px;top:125px;width:256px;height:160px">
    <svg width="44" height="44" viewBox="0 0 44 44" fill="none" stroke="#0054AA" stroke-width="2"><circle cx="30" cy="12" r="7"/><path d="M4 30h10l8 6h14M4 40h32M14 30l6-6"/></svg>
    <h3>Personalized, Human-Centered</h3><p>Identify And Mitigate Risks With Thorough Financial Analysis. We Help</p>
  </div>
  <div class="feature" style="left:884px;top:303px;width:256px;height:162px">
    <svg width="44" height="44" viewBox="0 0 44 44" fill="none" stroke="#0054AA" stroke-width="2"><path d="M4 32h12l8 6h16M4 42h36"/><circle cx="24" cy="14" r="9"/><path d="M20 14l3 3 6-6"/></svg>
    <h3>Transparency and Shared Decisions</h3><p>Identify And Mitigate Risks With Thorough Financial Analysis. We Help</p>
  </div>
</section>

<section class="faq">
  <div class="eyebrow" style="left:0;right:0;top:118px;text-align:center">fAQs</div>
  <h2 class="section-title" style="left:0;right:0;top:148px;text-align:center">Frequently Asked Questions</h2>

  <div class="q q-open" style="left:60px;top:237px">
    <span class="abs" style="right:16px;top:12px;font-size:22px">+</span>
    <h4>Lorem Ipsum Dolor Sit Amet Consectetur.</h4>
    <p>Lorem Ipsum Dolor Sit Amet Consectetur. Varius Tincidunt In Parturient Tristique Enim Amet Lacus Quis Sed. Nulla Congue Purus In Lacus Risus Molestie. Sed Fermentum Eu Nisl Enim Augue Quis. Felis Eu Tellus Porttitor Sit Congue Massa Eu</p>
    <p style="color:#fff;margin-top:8px">Read More ››</p>
  </div>
  <div class="q" style="left:426px;top:237px">Lorem Ipsum Dolor Sit Amet Consectetur.</div>
  <div class="q" style="left:792px;top:237px">Lorem Ipsum Dolor Sit Amet Consectetur.</div>
  <div class="q" style="left:426px;top:367px">Lorem Ipsum Dolor Sit Amet Consectetur.</div>
  <div class="q" style="left:792px;top:367px">Lorem Ipsum Dolor Sit Amet Consectetur.</div>
</section>

<section class="contact">
  <h2 class="section-title" style="left:0;right:0;top:46px;text-align:center">Contact Us</h2>
  <div class="abs" style="left:212px;top:133px;width:918px;height:540px;background:var(--white);border-radius:8px;box-shadow:0 6px 30px rgba(0,0,0,.14)"></div>
  <div class="ph" style="left:232px;top:198px;width:458px;height:410px;border-radius:6px;background:linear-gradient(135deg,#0b1c3a,#1e4c86 50%,#0a1a35)" role="img" aria-label="Médico examinando modelo 3D do corpo humano em tela"></div>
  <div class="abs" style="left:72px;top:273px;width:293px;height:250px;background:var(--white);border-radius:16px;box-shadow:0 6px 24px rgba(0,0,0,.15)">
    <svg class="abs" style="left:24px;top:30px" width="52" height="52" viewBox="0 0 52 52"><rect width="52" height="52" rx="10" fill="#0054AA"/><path d="M26 12a10 10 0 0 0-10 10c0 8 10 18 10 18s10-10 10-18a10 10 0 0 0-10-10z" fill="#fff"/><circle cx="26" cy="22" r="4" fill="#0054AA"/></svg>
    <div class="abs" style="left:88px;top:36px;font-size:13px;line-height:1.4">1480 Rua das Acácias,<br>Porto Verde 83470</div>
    <svg class="abs" style="left:24px;top:106px" width="52" height="52" viewBox="0 0 52 52"><rect width="52" height="52" rx="10" fill="#0054AA"/><path d="M18 14l6 1 2 7-4 3a16 16 0 0 0 7 7l3-4 7 2 1 6c-2 3-6 3-9 2a26 26 0 0 1-14-14c-1-3-1-7 1-10z" fill="#fff"/></svg>
    <div class="abs" style="left:88px;top:110px;font-size:14px;line-height:1.9">(480) 555-0147<br>(252) 555-0189</div>
    <svg class="abs" style="left:24px;top:180px" width="52" height="52" viewBox="0 0 52 52"><rect width="52" height="52" rx="10" fill="#0054AA"/><rect x="13" y="17" width="26" height="18" rx="2" fill="#fff"/><path d="M13 19l13 9 13-9" fill="none" stroke="#0054AA" stroke-width="2"/></svg>
    <div class="abs" style="left:88px;top:186px;font-size:13px;line-height:1.4">ana.souza@exa<br>mple.com</div>
  </div>

  <div class="abs" style="left:730px;top:232px;font-family:Inter,sans-serif;font-size:38px">Contact From</div>
  <span class="field-label" style="left:730px;top:326px">Full Name</span>
  <span class="field-line" style="left:730px;top:350px;width:168px"></span>
  <span class="field-label" style="left:932px;top:326px">Last Name</span>
  <span class="field-line" style="left:932px;top:350px;width:168px"></span>
  <span class="field-label" style="left:730px;top:372px">Email</span>
  <span class="field-line" style="left:730px;top:396px;width:168px"></span>
  <span class="field-label" style="left:932px;top:372px">Address</span>
  <span class="field-line" style="left:932px;top:396px;width:168px"></span>
  <span class="field-label" style="left:730px;top:418px">Messages</span>
  <div class="abs" style="left:730px;top:443px;width:370px;height:145px;border:1px solid #6d7480;border-radius:14px"></div>
  <div class="btn btn-blue" style="left:730px;top:608px;width:370px;height:44px">Submit</div>
</section>

<footer class="footer">
  <div class="abs logo" style="left:60px;top:80px;font-size:58px">LOGO</div>
  <p class="abs" style="left:60px;top:168px;width:400px;font-size:14px;line-height:1.65">Lorem Ipsum Dolor Sit Amet Consectetur. Habitasse Sed Commodo Dictumst Tristique. Senectus Adipiscing Aliquam Id Cras</p>
  <div class="abs" style="left:805px;top:165px;width:225px;height:38px;border:1px solid rgba(255,255,255,.7);border-radius:8px;font-size:12px;padding:10px 20px">Your Name</div>
  <div class="abs" style="left:1038px;top:165px;width:102px;height:38px;border-radius:8px;background:var(--white);color:var(--navy);font-size:13px;font-weight:600;text-align:center;line-height:38px">Submit</div>
  <span class="abs" style="left:64px;top:300px;width:28px;height:28px;border-radius:50%;border:2px solid #fff"></span>
  <span class="abs" style="left:118px;top:300px;width:28px;height:28px;border-radius:50%;border:2px solid #fff"></span>
  <span class="abs" style="left:172px;top:300px;width:28px;height:28px;border-radius:50%;border:2px solid #fff"></span>
  <div class="abs" style="left:895px;top:308px;font-size:13px;text-decoration:underline">Copy Right @ All Right Received By</div>
</footer>
<nav class="footer-nav">
  <a style="left:480px">Home</a>
  <a style="left:563px">Dr. Renato Vilhena</a>
  <a style="left:730px">Serviços</a>
  <a style="left:830px">Nossa Abordagem</a>
  <a style="left:1010px">Why Choose Me</a>
</nav>

</body>
</html>
```